Kestrelwood Pathways Agency business cards

Australian company about to start offering its services. We recruit international students to come to study English, vocational education and postgraduate courses in Australia. We help them find the institution and select the right city they want to come to Australia. We are a young, online oriented and supportive agency. Our clients are between 18 and 35 years old, mainly University students, young professionals or people with work experience. We provide much more information that any other agency offer. We administrate a Facebook group with more than 11.000 members that daily ask questions about general information when coming to Australia, while they are here and even after they leave the country

Target Market(s)

International students from South America, Central America and Europe

Industry/Entity Type

Student

Contact Information for Business Card

Tomas Brevik
Managing Director
tomas@velmorin.com.au
www.velmorin.com.au
+61 491058263
Melbourne, Australia

Font styles to use
Serif
Sans Serif

Colors

Designer to choose colors to be used in the design.

Requirements
Must have
• Horizontal design
• Standard business card size and shape. If font uses green or yellow colours, they will have to match the ones from the logo
Nice to have
• UPDATE: Use the contents of the green image to design one of the card sides. Use our logo in the background of that side as watermark.
• Passport image, or immigration stamps. A picture of the Yarra River (from Melbourne) would be cool as well.
Should not have
• Non-standard business card size and shape
• Not black as the background colour of any sides as we are not a VIP agency or a hight class service. We are orientes to young people and they like colours, pictures, something attractive.
• Vertical design
• NO YELLOW or BLACK AS THE BACKGROUND COLOUR OF ANY SIDE OF THE BIZ CARD

```html
<!DOCTYPE html>
<html lang="en">
<head>
<meta charset="utf-8">
<title>Kestrelwood Pathways Agency – Business Cards</title>
<link rel="stylesheet" href="https://fonts.googleapis.com/css2?family=Source+Sans+3:wght@400;600;700&family=Gochi+Hand&display=swap">
<style>
  :root {
    --stage: #3a3a3c;
    --card-white: #ffffff;
    --brand-green: #0f5a30;
    --brand-yellow: #e8b71a;
    --text-light: #ffffff;
  }
  * { margin: 0; padding: 0; box-sizing: border-box; }
  html, body {
    width: 1200px; height: 900px; overflow: hidden;
    background: var(--stage);
    font-family: "Source Sans 3", "Myriad Pro", Arial, sans-serif;
  }
  .canvas { position: relative; width: 1200px; height: 900px; }

  .card {
    position: absolute;
    width: 525px; height: 300px;
    border-radius: 3px;
    box-shadow: 0 12px 30px rgba(0,0,0,.45);
    overflow: hidden;
  }

  /* Front side */
  .card--front {
    left: 95px; top: 105px;
    background: var(--card-white);
    display: flex; align-items: center; justify-content: center;
  }
  .brand-mark {
    display: flex; align-items: center; gap: 10px;
    font-weight: 700; font-size: 40px; color: var(--brand-green);
    letter-spacing: .5px;
  }
  .brand-mark__dot {
    width: 16px; height: 16px; border-radius: 50%;
    background: var(--brand-green);
  }

  /* Back side */
  .card--back {
    left: 585px; top: 495px;
    background: var(--brand-green);
    color: var(--text-light);
  }
  .back-brand {
    position: absolute; left: 26px; bottom: 30px;
    font-weight: 700; font-size: 46px; line-height: 1;
    color: var(--text-light);
  }
  .contact {
    position: absolute; left: 290px; top: 46px;
    font-size: 13.5px; line-height: 1.2;
  }
  .contact__name { font-weight: 700; }
  .contact__group + .contact__group { margin-top: 14px; }
  .tagline {
    position: absolute; right: 24px; bottom: 30px;
    font-family: "Gochi Hand", "Comic Sans MS", cursive;
    font-size: 22px; color: var(--brand-yellow);
  }
</style>
</head>
<body>
<main class="canvas">
  <section class="card card--front" aria-label="Business card front">
    <div class="brand-mark">
      <span class="brand-mark__dot"></span>
      <span class="brand-mark__name">Kestrelwood</span>
    </div>
  </section>

  <section class="card card--back" aria-label="Business card back">
    <div class="contact">
      <div class="contact__group">
        <div class="contact__name">Tomas Brevik</div>
        <div>Managing Director</div>
      </div>
      <div class="contact__group">
        <div>Kestrelwood Pathways</div>
        <div>Melbourne, Australia</div>
      </div>
      <div class="contact__group">
        <div>+61 491058263</div>
        <div>tomas@velmorin.com.au</div>
        <div>www.velmorin.com.au</div>
      </div>
    </div>
    <div class="back-brand">Kestrelwood</div>
    <div class="tagline">Hacemos más por ti!</div>
  </section>
</main>
</body>
</html>
```